Business Card Design

i am looking a business card for a car rental company long with Taxi service also a logo.

what is the latest with my project

Industry/Entity Type

Business

Contact Information for Business Card

name of the Company is Kestrel Bay Motor Leasing and Taxi Services
Address: Old Road Village, St. Mary's Parish Antigua
Tele# 555-0142/5550187-555-0163
Email: lorimbeck@quillmarsh.test

Font styles to use
Script

```html
<!DOCTYPE html>
<html lang="en">
<head>
<meta charset="utf-8">
<title>Kestrel Bay Motor Leasing and Taxi Services – Business Card</title>
<link href="https://fonts.googleapis.com/css2?family=Courgette&display=swap" rel="stylesheet">
<style>
  :root {
    --card-black: #000000;
    --gold: #b98a3c;
    --gold-light: #d9b46a;
    --gold-edge: #e6d3a6;
    --text-white: #f2f2f2;
    --script: "Courgette", cursive;
  }
  html, body {
    margin: 0;
    padding: 0;
    width: 1200px;
    height: 857px;
    overflow: hidden;
    background: var(--card-black);
  }
  .card {
    position: relative;
    width: 1200px;
    height: 857px;
    background: var(--card-black);
    font-family: var(--script);
    color: var(--text-white);
  }
  .brand-mark {
    position: absolute;
    left: 40px;
    top: 95px;
    width: 130px;
    height: 130px;
    border: 6px solid var(--gold);
    border-radius: 50%;
    box-sizing: border-box;
  }
  .company-name {
    position: absolute;
    left: 242px;
    top: 158px;
    margin: 0;
    font-size: 40px;
    font-weight: 400;
    white-space: nowrap;
    color: var(--text-white);
    line-height: 1;
  }
  .name-rule {
    position: absolute;
    left: 238px;
    top: 214px;
    width: 962px;
    height: 6px;
    background: var(--gold);
    border-top: 1px solid var(--gold-edge);
    border-bottom: 1px solid var(--gold-edge);
    box-sizing: border-box;
  }
  .contact-list {
    position: absolute;
    left: 48px;
    top: 500px;
    margin: 0;
    padding: 0;
    list-style: none;
  }
  .contact-item {
    display: flex;
    align-items: center;
    height: 38px;
    margin-bottom: 38px;
    font-size: 31px;
    white-space: nowrap;
  }
  .contact-icon {
    width: 36px;
    height: 36px;
    margin-right: 22px;
    flex: none;
  }
  .contact-icon path, .contact-icon rect { fill: var(--gold); }
  .footer-band {
    position: absolute;
    left: 0;
    bottom: 0;
    width: 1200px;
    height: 42px;
    background: var(--gold);
    border-top: 3px solid var(--gold-edge);
    box-sizing: border-box;
  }
</style>
</head>
<body>
  <main class="card">
    <div class="brand-mark" aria-hidden="true"></div>
    <h1 class="company-name">Kestrel Bay Motor Leasing and Taxi Services</h1>
    <div class="name-rule"></div>

    <ul class="contact-list">
      <li class="contact-item">
        <svg class="contact-icon" viewBox="0 0 36 36" aria-hidden="true">
          <path d="M4 13c0-5 6-7 14-7s14 2 14 7v2h-7v-3c-2-1-5-1-7-1s-5 0-7 1v3H4z"/>
          <path d="M9 16l3-3h12l3 3v12c0 1-1 2-2 2H11c-1 0-2-1-2-2z"/>
        </svg>
        <span>555-0142/5550187-555-0163</span>
      </li>
      <li class="contact-item">
        <svg class="contact-icon" viewBox="0 0 36 36" aria-hidden="true">
          <path d="M2 8h32v20H2z M5 11v1l13 9 13-9v-1z M5 15v10h26V15L18 24z" fill-rule="evenodd"/>
        </svg>
        <span>lorimbeck@quillmarsh.test</span>
      </li>
      <li class="contact-item">
        <svg class="contact-icon" viewBox="0 0 36 36" aria-hidden="true">
          <path d="M18 2c-6 0-11 5-11 11 0 8 11 21 11 21s11-13 11-21c0-6-5-11-11-11zm0 6a5 5 0 1 1 0 10 5 5 0 0 1 0-10z" fill-rule="evenodd"/>
        </svg>
        <span>Heron Point Village . St . Clement’s Parish Antigue</span>
      </li>
    </ul>

    <div class="footer-band"></div>
  </main>
</body>
</html>
```